Paint Factory Needs Bucket Designs

I have paint factory and I want Paint buckets designs. The buckets should be the below sizes:

1 ltr
4 ltrs
10 ltrs
20 ltrs

```html
<!DOCTYPE html>
<html lang="en">
<head>
<meta charset="utf-8">
<title>Veluma Paints – Advanced Cement Primer 4L Label</title>
<link rel="stylesheet" href="https://fonts.googleapis.com/css2?family=Jost:ital,wght@0,300;0,400;0,500;0,600;1,300&family=Pinyon+Script&display=swap">
<style>
  :root {
    --page: #ffffff;
    --navy-deep: #16304f;
    --navy: #1e3d63;
    --navy-ink: #1b3350;
    --silver-light: #eceded;
    --silver: #cfd1d5;
    --silver-dark: #a9acb2;
    --panel-light: #e4e5e8;
    --panel: #c8cacf;
    --brand-silver: #cdd0d5;
    --stroke-white: #f4f4f6;
  }
  * { margin: 0; padding: 0; box-sizing: border-box; }
  html, body { width: 1200px; height: 831px; overflow: hidden; background: var(--page); }
  .canvas { position: relative; width: 1200px; height: 831px; background: var(--page); }

  .label {
    position: absolute; left: 170px; top: 90px; width: 860px; height: 650px;
    border-radius: 6px; overflow: hidden;
    background: linear-gradient(90deg, var(--silver-dark) 0%, var(--silver-light) 30%, var(--silver) 60%, var(--silver-light) 80%, var(--silver-dark) 100%);
    box-shadow: 0 10px 30px rgba(0,0,0,0.12);
  }
  .brand-band {
    position: absolute; left: 0; top: 0; width: 100%; height: 380px;
    background: linear-gradient(90deg, var(--navy-deep) 0%, var(--navy) 45%, #2c4f78 75%, var(--navy-deep) 100%);
    display: flex; flex-direction: column; align-items: center; justify-content: center;
  }
  .brand-dot {
    width: 26px; height: 26px; border-radius: 50%;
    background: var(--brand-silver); margin-bottom: 26px;
  }
  .brand-name {
    font-family: "Jost", sans-serif; font-weight: 600; color: var(--brand-silver);
    text-align: center; line-height: 1.05; letter-spacing: 2px;
  }
  .brand-name .line-1 { display: block; font-size: 72px; }
  .brand-name .line-2 { display: block; font-size: 48px; }

  .product-panel {
    position: absolute; left: 170px; top: 380px; width: 560px; height: 270px;
    background: linear-gradient(90deg, var(--panel-light) 0%, var(--panel-light) 40%, var(--panel) 100%);
  }
  .panel-rule {
    position: absolute; left: 18px; top: 22px; width: 3px; height: 190px;
    background: var(--navy-ink);
  }
  .product-copy { position: absolute; left: 38px; top: 22px; color: var(--navy-ink); font-family: "Jost", sans-serif; }
  .product-kicker { font-size: 24px; font-weight: 300; font-style: italic; letter-spacing: 1px; }
  .product-name { font-size: 52px; font-weight: 600; letter-spacing: 2px; line-height: 1.05; white-space: nowrap; }
  .product-base { font-size: 28px; font-weight: 400; letter-spacing: 1px; line-height: 1.1; }

  .brush-stroke {
    position: absolute; left: 300px; top: 120px; width: 240px; height: 120px;
    border-radius: 50% 40% 45% 50%;
    background: radial-gradient(ellipse at 45% 50%, var(--stroke-white) 0%, #e3e4e7 60%, rgba(220,221,225,0) 100%);
  }

  .product-meta { position: absolute; left: 38px; top: 178px; color: var(--navy-ink); font-family: "Jost", sans-serif; }
  .meta-premium { font-family: "Pinyon Script", cursive; font-size: 34px; line-height: 1; }
  .meta-use { font-size: 18px; font-weight: 400; letter-spacing: 0.5px; margin-top: 2px; }
  .meta-volume { font-size: 30px; font-weight: 400; margin-top: 2px; line-height: 1; }
</style>
</head>
<body>
  <div class="canvas">
    <div class="label">
      <header class="brand-band">
        <span class="brand-dot"></span>
        <h1 class="brand-name"><span class="line-1">VELUMA</span><span class="line-2">PAINTS</span></h1>
      </header>

      <section class="product-panel">
        <span class="panel-rule"></span>
        <div class="product-copy">
          <p class="product-kicker">ADVANCED</p>
          <h2 class="product-name">CEMENT PRIMER</h2>
          <p class="product-base">WATER BASE</p>
        </div>
        <div class="brush-stroke" role="img" aria-label="White brush stroke of primer paint"></div>
        <div class="product-meta">
          <p class="meta-premium">Premium</p>
          <p class="meta-use">INTERIOR &amp; EXTERIOR</p>
          <p class="meta-volume">4L</p>
        </div>
      </section>
    </div>
  </div>
</body>
</html>
```